Post it Note design

POST-IT NOTE DESIGN (CONTENT)
Size recommended: 4x6 for handwriting space.
Header (Bold):
Lighting Issue Detected on Your Property
Sub-header:
During our routine night inspection, we noted the following item(s):
Checkbox List:
⬜ Building Lights Out
⬜ Pole Lights Out
⬜ Sign Not Illuminated
⬜ Other ________________________
Action Line:
We can provide a quote or dispatch service right away.
Area for notes
Contact Block (Bold & Centered):
Brightwell Fixture Care Inc.
Service@BrightwellFixtureCare.com
www.BrightwellFixtureCare.com
877-514-6082
Industry/Entity Type
Electrical lighting
Colors
Designer to choose colors to be used in the design.
Look and feel
Each slider illustrates characteristics of the customer's brand and the style your logo design should communicate.

```html
<!DOCTYPE html>
<html lang="en">
<head>
<meta charset="utf-8">
<title>Brightwell Fixture Care – Inspection Note</title>
<link rel="stylesheet" href="https://fonts.googleapis.com/css2?family=Oswald:wght@500;700&family=Montserrat:wght@400;500;700;800&display=swap">
<style>
  :root {
    --red: #e31b23;
    --navy: #283583;
    --ink: #111111;
    --paper: #ffffff;
    --stage: #e6e6e6;
    --box-line: #8d8d8d;
  }
  * { box-sizing: border-box; margin: 0; padding: 0; }
  html, body { width: 1200px; height: 1200px; overflow: hidden; background: var(--stage); }
  .note {
    position: absolute; left: 0; top: 200px; width: 1200px; height: 800px;
    background: var(--paper); font-family: "Montserrat", sans-serif; color: var(--navy);
  }
  .brand {
    position: absolute; left: 58px; top: 40px; width: 400px; height: 190px;
    display: flex; align-items: center; justify-content: center; text-align: center;
    font-family: "Oswald", sans-serif; font-weight: 700; color: var(--red);
    font-size: 62px; line-height: 1.05; text-transform: uppercase;
  }
  .truck-photo {
    position: absolute; left: 727px; top: 11px; width: 440px; height: 238px;
    background: linear-gradient(160deg, #f4f4f4 0%, #dcdcdc 55%, #b9b9b9 100%);
  }
  .headline-band {
    position: absolute; left: 0; top: 248px; width: 1200px; height: 93px;
    background: var(--red); border-top: 3px solid var(--navy); border-bottom: 3px solid var(--navy);
    display: flex; align-items: center; justify-content: center;
  }
  .headline {
    font-family: "Oswald", sans-serif; font-weight: 700; color: var(--paper);
    font-size: 63px; letter-spacing: -0.5px; text-transform: uppercase;
    text-shadow: 2px 3px 3px rgba(0,0,0,.35);
  }
  .intro {
    position: absolute; left: 0; top: 356px; width: 1200px; text-align: center;
    font-size: 22px; font-weight: 500; text-transform: uppercase; letter-spacing: 0.2px;
  }
  .intro strong { font-weight: 800; }
  .check {
    position: absolute; width: 417px; height: 40px; border: 2px solid var(--box-line);
    display: flex; align-items: center; gap: 12px; padding-left: 8px;
    font-size: 25px; font-weight: 800; text-transform: uppercase;
  }
  .check .tick-box { width: 25px; height: 25px; border: 2px solid var(--ink); flex: none; }
  .check .blank { flex: 1; margin-right: 20px; border-bottom: 2px solid var(--navy); align-self: flex-end; margin-bottom: 7px; }
  .c1 { left: 250px; top: 405px; left: 143px; }
  .c2 { left: 143px; top: 470px; }
  .c3 { left: 640px; top: 405px; }
  .c4 { left: 640px; top: 470px; }
  .action {
    position: absolute; left: 0; top: 540px; width: 560px; height: 111px; background: var(--navy);
    color: var(--paper); display: flex; align-items: center; justify-content: flex-end; padding-right: 20px; gap: 12px;
  }
  .action .lead { font-size: 22px; font-weight: 500; line-height: 1.05; text-align: right; text-transform: uppercase; margin-top: -10px; }
  .action .main { display: flex; flex-direction: column; align-items: flex-end; }
  .action .big { font-family: "Oswald", sans-serif; font-weight: 700; font-size: 50px; line-height: 1; letter-spacing: -1.5px; text-transform: uppercase; }
  .action .tail { font-size: 21px; font-weight: 500; text-transform: uppercase; letter-spacing: 0.5px; }
  .notes {
    position: absolute; left: 640px; top: 540px; width: 560px; height: 111px;
    border: 2px solid var(--ink); border-right: none; padding: 14px 0 0 12px;
    color: var(--ink); font-size: 19px; line-height: 30px;
  }
  .notes .rule { display: block; width: 470px; border-bottom: 2px dotted var(--ink); height: 22px; margin-bottom: 8px; }
  .notes .label { position: absolute; top: 14px; left: 12px; background: var(--paper); padding-right: 2px; line-height: 20px; text-transform: uppercase; }
  .footer-band {
    position: absolute; left: 0; top: 692px; width: 1200px; height: 44px; display: flex; align-items: center;
  }
  .footer-band .bar { flex: 1; height: 44px; background: var(--red); }
  .footer-band .name { padding: 0 12px; color: var(--ink); font-weight: 800; font-size: 36px; letter-spacing: 1px; text-transform: uppercase; white-space: nowrap; }
  .contact {
    position: absolute; left: 0; top: 750px; width: 1200px; display: flex; justify-content: center; align-items: center; gap: 6px;
    color: var(--ink); font-weight: 700; font-size: 19px; white-space: nowrap;
  }
  .contact svg { width: 20px; height: 20px; flex: none; }
  .contact .sep { margin: 0 4px; }
</style>
</head>
<body>
<main class="note">
  <div class="brand">Brightwell Fixture Care Inc.</div>
  <div class="truck-photo" role="img" aria-label="Photo of a white bucket truck with traffic cones"></div>

  <div class="headline-band"><h1 class="headline">Lighting Issue Detected on Your Property</h1></div>

  <p class="intro">During our <strong>routine night inspection</strong>, we noted the following item(s):</p>

  <div class="check c1"><span class="tick-box"></span>Building Lights Out</div>
  <div class="check c2"><span class="tick-box"></span>Pole Lights Out</div>
  <div class="check c3"><span class="tick-box"></span>Sign Not Illuminated</div>
  <div class="check c4"><span class="tick-box"></span>Other<span class="blank"></span></div>

  <div class="action">
    <div class="lead">We can<br>provide a</div>
    <div class="main">
      <span class="big">Quote or Dispatch</span>
      <span class="tail">Service right away.</span>
    </div>
  </div>

  <div class="notes">
    <span class="rule"></span><span class="rule"></span><span class="rule"></span>
    <span class="label">Notes</span>
  </div>

  <div class="footer-band"><span class="bar"></span><span class="name">Brightwell Fixture Care Inc.</span><span class="bar"></span></div>

  <div class="contact">
    <svg viewBox="0 0 20 20"><rect x="2" y="5" width="16" height="11" fill="none" stroke="#283583" stroke-width="2"/><path d="M2 5l8 6 8-6" fill="none" stroke="#283583" stroke-width="2"/></svg>
    <span>Service@BrightwellFixtureCare.com</span><span class="sep">|</span>
    <svg viewBox="0 0 20 20"><circle cx="10" cy="10" r="8" fill="none" stroke="#283583" stroke-width="1.6"/><ellipse cx="10" cy="10" rx="3.5" ry="8" fill="none" stroke="#283583" stroke-width="1.4"/><path d="M2 10h16M3.5 6h13M3.5 14h13" stroke="#283583" stroke-width="1.2"/></svg>
    <span>www.BrightwellFixtureCare.com</span><span class="sep">|</span>
    <svg viewBox="0 0 20 20"><path d="M5 2l3 4-2 2c1 2.5 3 4.5 5.5 5.5l2-2 4 3-2 3C9 17 3 11 2.5 5z" fill="#283583"/></svg>
    <span>877-514-6082</span>
  </div>
</main>
</body>
</html>
```